Beauty Clinic Treatment Menu (Lumen Nails & Beauty)

Needing a treatment menu designed for a beauty clinic in Whitianga, New Zealand. Like the colours grey, pink, white.
Elegant, Modern and feminine

Lumen Nails & Beauty
Dana Pirrett
Room1, 17 Corbel Street
Whitianga
0271836042
Dana.lumen@mailbay.example
lumenbeauty.example.nz

Target Market(s)

Females

Industry/Entity Type

Beauty Salon

Font styles to use
Serif

Colors

Designer to choose colors to be used in the design.

Requirements
Must have
• Chatterbook and Snapgrid logo

```html
<!DOCTYPE html>
<html lang="en">
<head>
<meta charset="utf-8">
<title>Lumen Nails &amp; Beauty – Treatment Menu</title>
<link rel="stylesheet" href="https://fonts.googleapis.com/css2?family=Bodoni+Moda:ital,opsz,wght@0,6..96,400;0,6..96,600;1,6..96,400&display=swap">
<style>
  :root{
    --pink:#eeaac3;
    --pink-deep:#e68aad;
    --grey:#4a4c4f;
    --white:#ffffff;
    --ink:#2f3033;
    --stage:#d8d8d8;
    --serif:"Bodoni Moda", Georgia, serif;
  }
  *{box-sizing:border-box;margin:0;padding:0}
  html,body{width:1020px;height:1200px;overflow:hidden}
  body{background:var(--stage);font-family:var(--serif);color:var(--ink);position:relative}

  .sheet{position:absolute;left:135px;width:750px;height:560px;background:var(--white);overflow:hidden;box-shadow:0 6px 18px rgba(0,0,0,.18)}
  .sheet--outside{top:26px}
  .sheet--inside{top:614px}
  .sheet__bg{position:absolute;inset:0}
  .panel{position:absolute;top:0;width:250px;height:560px}
  .panel--1{left:0}.panel--2{left:250px}.panel--3{left:500px}

  /* brand name */
  .brand{position:absolute;left:0;right:0;display:flex;flex-direction:column;align-items:center}
  .brand__row{display:flex;align-items:center;gap:8px}
  .brand__dot{width:12px;height:12px;border-radius:50%;background:var(--pink-deep)}
  .brand__name{font-size:38px;color:var(--grey);letter-spacing:1px}
  .brand__sub{font-size:8px;color:var(--grey);letter-spacing:1px;margin-top:2px}
  .brand--small .brand__name{font-size:20px}
  .brand--small .brand__dot{width:8px;height:8px}
  .brand--small .brand__sub{font-size:6px}

  /* about */
  .about__title{position:absolute;top:26px;left:0;right:0;text-align:center;font-size:10px;letter-spacing:2px}
  .about__title::after{content:"";display:block;width:90px;height:1px;background:var(--ink);margin:4px auto 0}
  .about__story{position:absolute;top:54px;left:20px;right:20px;font-size:9.5px;line-height:13px;text-align:justify}
  .about__portrait{position:absolute;top:228px;left:85px;width:80px;height:80px;background:linear-gradient(160deg,#e9e6e3,#b48a6e 60%,#3a3030)}
  .about__salon{position:absolute;top:330px;left:20px;right:20px;font-size:9.5px;line-height:13px;text-align:center}
  .partner{position:absolute;top:478px;left:22px;display:flex;align-items:center;gap:7px;color:var(--white)}
  .partner__square{width:16px;height:16px;background:var(--white)}
  .partner__name{font-size:13px;line-height:14px}
  .partner-badge{position:absolute;top:470px;left:190px;width:40px;height:40px;border-radius:50%;background:var(--pink)}

  /* contact */
  .contact{position:absolute;top:314px;left:28px;right:10px;list-style:none}
  .contact li{display:flex;align-items:center;gap:9px;font-size:9px;line-height:11px;margin-bottom:9px}
  .contact svg{flex:0 0 18px;width:18px;height:18px}
  .social{position:absolute;top:448px;left:0;right:0;text-align:center;color:var(--white)}
  .social__links{display:flex;justify-content:center;gap:16px;font-size:10px}
  .social__link{display:flex;align-items:center;gap:5px}
  .social__dot{width:12px;height:12px;border-radius:50%;background:var(--white)}
  .social__handle{font-size:15px;margin-top:10px;letter-spacing:.5px}
  .rule{display:block;width:80px;height:3px;background:var(--pink);margin:7px auto 0}

  /* cover */
  .services{position:absolute;top:160px;left:18px;width:214px;display:grid;grid-template-columns:1fr 1fr;gap:8px}
  .service{position:relative;height:104px}
  .service--facials{background:linear-gradient(135deg,#c9c6d6,#f4f2f6 55%,#8e8aa0)}
  .service--tinting{background:linear-gradient(135deg,#d7b49c,#f3e4da 50%,#8a5c44)}
  .service--waxing{background:linear-gradient(135deg,#f7f3ef,#e9c7ad 55%,#c89b7e)}
  .service--nails{background:linear-gradient(135deg,#f9ecec,#e8c3b2 55%,#3b3f9e)}
  .tag{display:inline-block;background:var(--grey);color:var(--white);font-size:9px;letter-spacing:1.5px;padding:3px 8px 4px;text-align:center}
  .tag::after{content:"";display:block;height:1.5px;background:var(--pink);margin:2px 6px 0}
  .tag--pink{background:var(--pink-deep)}
  .tag--pink::after{background:var(--grey)}
  .service .tag{position:absolute;bottom:4px;left:50%;transform:translateX(-50%)}
  .tagline{position:absolute;top:440px;left:0;right:0;text-align:center;color:var(--white);font-size:15px;line-height:19px}

  /* menu lists */
  .menu-tag{position:absolute;left:0;right:0;text-align:center}
  .menu-tag .tag{font-size:11px;padding:4px 16px 5px}
  .price-list{position:absolute;left:20px;right:20px;font-size:9.5px;line-height:15px}
  .price-list h3{font-weight:400;font-size:10px;letter-spacing:1.5px;margin-top:6px}
  .price-list h3:first-child{margin-top:0}
  .price-list p{font-size:8.5px;line-height:11px}
  .row{display:flex;justify-content:space-between;border-bottom:1px dotted var(--ink)}
  .row--indent{padding-left:10px}

  .menu-title{position:absolute;top:14px;left:0;right:0;text-align:center;font-size:46px;line-height:50px;color:var(--pink);letter-spacing:3px}
  .menu-bar{position:absolute;top:70px;left:70px;width:110px;height:4px;background:var(--grey)}
  .facials{position:absolute;top:132px;left:18px;right:18px;color:var(--white);list-style:none}
  .facial{margin-bottom:13px}
  .facial__head{display:flex;justify-content:space-between;font-size:12.5px;border-bottom:1px dotted var(--white);padding-bottom:1px}
  .facial__time{font-size:8.5px;margin-top:2px}
  .facial__desc{font-size:8.5px;line-height:11px}

  .peony{position:absolute;top:0;left:0;width:250px;height:115px;background:radial-gradient(ellipse at 60% 40%,#f6b9c9,#f9dde5 55%,#fdf3f5)}
</style>
</head>
<body>

<section class="sheet sheet--outside" aria-label="Brochure outside">
  <svg class="sheet__bg" viewBox="0 0 750 560" aria-hidden="true">
    <path d="M0 280 C120 250 200 300 300 300 C420 300 450 225 540 205 C620 190 690 215 750 230 L750 560 L0 560Z" fill="var(--pink)"/>
    <path d="M0 445 C160 430 280 445 420 420 C560 395 640 380 750 355 L750 560 L0 560Z" fill="var(--grey)"/>
  </svg>

  <div class="panel panel--1">
    <h2 class="about__title">ABOUT LUMEN</h2>
    <p class="about__story">In 2014 I graduated from my Diploma in Beauty therapy at New Zealand's leading beauty school, Crest. Since then I have worked at two amazing beauty salons, both which taught me valuable skills and information about beauty and nail therapies. I enjoy learning new skills and therapies, keeping up with the latest beauty trends, interacting with my clients and meeting new people. In early 2016 I made the decision to move to Whitianga to live with my partner, and I am loving the relaxed lifestyle!</p>
    <div class="about__portrait" role="img" aria-label="Portrait photo of the therapist, Dana Pirrett"></div>
    <p class="about__salon">Lumen Nails &amp; Beauty is a modern salon located in the town centre of beautiful Whitianga. Offering Facials, Waxing, Tinting and Nails this is your one stop shop for all your beauty needs! Lumen uses only the best products available to ensure that every client is getting what they deserve.</p>
    <div class="partner">
      <span class="partner__square"></span>
      <span class="partner__name">Orvane<br>Skin Technology</span>
    </div>
    <div class="partner-badge" role="img" aria-label="Partner badge"></div>
  </div>

  <div class="panel panel--2">
    <div class="brand" style="top:110px">
      <div class="brand__row"><span class="brand__dot"></span><span class="brand__name">Lumen</span></div>
      <span class="brand__sub">Nails &amp; Beauty</span>
    </div>
    <ul class="contact">
      <li>
        <svg viewBox="0 0 18 18"><circle cx="9" cy="9" r="9" fill="var(--white)"/><path d="M6 5 L8 5 L8.6 7.4 L7.5 8.3 C8 9.5 8.5 10 9.7 10.5 L10.6 9.4 L13 10 L13 12 C9 12.5 5.5 9 6 5Z" fill="var(--pink-deep)"/></svg>
        027 183 6042
      </li>
      <li>
        <svg viewBox="0 0 18 18"><circle cx="9" cy="9" r="9" fill="var(--white)"/><rect x="4.5" y="6" width="9" height="6.5" fill="none" stroke="var(--pink-deep)" stroke-width="1.1"/><path d="M4.5 6 L9 9.6 L13.5 6" fill="none" stroke="var(--pink-deep)" stroke-width="1.1"/></svg>
        Dana.lumen@mailbay.example
      </li>
      <li>
        <svg viewBox="0 0 18 18"><circle cx="9" cy="9" r="9" fill="var(--white)"/><g fill="none" stroke="var(--pink-deep)" stroke-width="1"><circle cx="9" cy="9" r="4.6"/><ellipse cx="9" cy="9" rx="2" ry="4.6"/><path d="M4.4 9 H13.6"/></g></svg>
        www.lumenbeauty.example.nz
      </li>
      <li>
        <svg viewBox="0 0 18 18"><circle cx="9" cy="9" r="9" fill="var(--white)"/><path d="M9 14 C6.5 10.5 5.5 9 5.5 7.5 A3.5 3.5 0 0 1 12.5 7.5 C12.5 9 11.5 10.5 9 14Z" fill="var(--pink-deep)"/><circle cx="9" cy="7.5" r="1.3" fill="var(--white)"/></svg>
        Room1, 17 Corbel Street, Whitianga<br>(Above Keelson Sports)
      </li>
    </ul>
    <div class="social">
      <div class="social__links">
        <span class="social__link"><span class="social__dot"></span>Chatterbook</span>
        <span class="social__link"><span class="social__dot"></span>Snapgrid</span>
      </div>
      <p class="social__handle">lumennailsbeauty</p>
      <span class="rule"></span>
    </div>
  </div>

  <div class="panel panel--3">
    <div class="brand" style="top:50px">
      <div class="brand__row"><span class="brand__dot"></span><span class="brand__name">Lumen</span></div>
      <span class="brand__sub">Nails &amp; Beauty</span>
    </div>
    <div class="services">
      <div class="service service--facials" role="img" aria-label="Photo of facial cream and spa stones"><span class="tag">FACIALS</span></div>
      <div class="service service--tinting" role="img" aria-label="Close-up photo of a tinted brow and eye"><span class="tag">TINTING</span></div>
      <div class="service service--waxing" role="img" aria-label="Photo of smooth legs at a spa"><span class="tag tag--pink">WAXING</span></div>
      <div class="service service--nails" role="img" aria-label="Photo of a hand with blue painted nails"><span class="tag tag--pink">NAILS</span></div>
    </div>
    <p class="tagline">Your one stop shop<br>for all your beauty needs!</p>
    <span class="rule" style="position:absolute;top:492px;left:85px;margin:0"></span>
  </div>
</section>

<section class="sheet sheet--inside" aria-label="Brochure inside – treatment menu">
  <svg class="sheet__bg" viewBox="0 0 750 560" aria-hidden="true">
    <path d="M0 70 C80 60 160 40 250 90 L250 560 L0 560Z" fill="var(--pink)"/>
    <path d="M250 560 L250 112 L500 112 L500 560Z" fill="var(--grey)"/>
    <rect x="500" y="100" width="250" height="460" fill="var(--pink)"/>
  </svg>

  <div class="panel panel--1">
    <div class="brand brand--small" style="top:10px">
      <div class="brand__row"><span class="brand__dot"></span><span class="brand__name">Lumen</span></div>
      <span class="brand__sub">Nails &amp; Beauty</span>
    </div>
    <div class="menu-tag" style="top:52px"><span class="tag">NAILS</span></div>
    <div class="price-list" style="top:92px">
      <h3>MANICURE</h3>
      <div class="row row--indent"><span>Gel Polish</span><span>$ 45</span></div>
      <div class="row row--indent"><span>Regular Polish</span><span>$ 40</span></div>
      <h3>PEDICURE</h3>
      <div class="row row--indent"><span>Gel Polish</span><span>$ 45</span></div>
      <div class="row row--indent"><span>Regular Polish</span><span>$ 40</span></div>
      <h3>LUXURY PEDICURE</h3>
      <p>Includes: soak, exfoliation, heel rasping and massage.</p>
      <div class="row row--indent"><span>Gel Polish</span><span>$ 60</span></div>
      <div class="row row--indent"><span>Regular Polish</span><span>$ 55</span></div>
      <h3 class="row"><span>GEL REMOVAL &amp; NAIL TIDY</span><span>$ 25</span></h3>
      <h3>ADD ON</h3>
      <div class="row row--indent"><span>Gel Removal</span><span>$ 5</span></div>
      <div class="row row--indent"><span>Fortix (per layer)</span><span>$ 5</span></div>
      <div class="row row--indent"><span>Build Base Gel</span><span>$ 10</span></div>
      <div class="row row--indent"><span>Nail Art/ Glitter</span><span>SPOA</span></div>
    </div>
  </div>

  <div class="panel panel--2">
    <h1 class="menu-title">MENU</h1>
    <span class="menu-bar"></span>
    <div class="menu-tag" style="top:88px"><span class="tag tag--pink">FACIALS</span></div>
    <ul class="facials">
      <li class="facial">
        <div class="facial__head"><span>Deep Cleansing Facial</span><span>$ 75</span></div>
        <p class="facial__time">45 minutes</p>
        <p class="facial__desc">Removes build up of dead skin cells, leaves the skin feeling soft and hydrated.</p>
      </li>
      <li class="facial">
        <div class="facial__head"><span>Therapeutic Facial</span><span>$ 105</span></div>
        <p class="facial__time">60 minutes</p>
        <p class="facial__desc">Tailored to suit your skins specific needs.</p>
      </li>
      <li class="facial">
        <div class="facial__head"><span>Rejuvenation Facial</span><span>$ 120</span></div>
        <p class="facial__time">60 Minutes</p>
        <p class="facial__desc">Active yet gentle treatment that facilitates dermal rejuvenation.</p>
      </li>
      <li class="facial">
        <div class="facial__head"><span>35% Glycolic Facial</span><span>$ 120</span></div>
        <p class="facial__time">60 Minutes</p>
        <p class="facial__desc">Hydrating, deep exfoliation treatment improving skin texture and appearance.</p>
      </li>
      <li class="facial">
        <div class="facial__head"><span>Dermaplaning</span><span>$ 120</span></div>
        <p class="facial__desc">Creates a smooth and radiant skin surface. Also removes soft facial hairs.</p>
      </li>
    </ul>
  </div>

  <div class="panel panel--3">
    <div class="peony" role="img" aria-label="Soft photo of a pale pink peony"></div>
    <div class="menu-tag" style="top:112px"><span class="tag">EYES</span></div>
    <div class="price-list" style="top:146px">
      <div class="row"><span>Aurel Lash Lift</span><span>$ 115</span></div>
      <div class="row"><span>Eyebrow Shape</span><span>$ 19</span></div>
      <div class="row"><span>Eyebrow Tint</span><span>$ 18</span></div>
      <div class="row"><span>Eyelash Tint</span><span>$ 25</span></div>
      <div class="row"><span>Eye Trio</span><span>$ 45</span></div>
    </div>
    <div class="menu-tag" style="top:236px"><span class="tag">FACE</span></div>
    <div class="price-list" style="top:270px">
      <div class="row"><span>Lip</span><span>$ 15</span></div>
      <div class="row"><span>Chin</span><span>$ 15</span></div>
    </div>
    <div class="menu-tag" style="top:312px"><span class="tag">BODY</span></div>
    <div class="price-list" style="top:346px">
      <div class="row"><span>Under Arm</span><span>$ 20</span></div>
      <div class="row"><span>1/2 Leg</span><span>$ 35</span></div>
      <div class="row"><span>Full Leg</span><span>$ 55</span></div>
      <div class="row"><span>1/2 Arm</span><span>$ 30</span></div>
      <div class="row"><span>Full Arm</span><span>$ 40</span></div>
      <div class="row"><span>Bikini</span><span>$ 28</span></div>
      <div class="row"><span>Extended Bikini</span><span>$ 38</span></div>
      <div class="row"><span>Brazilian (1st Time)</span><span>$ 65</span></div>
      <div class="row"><span>Brazilian (4-6 Weeks)</span><span>$ 50</span></div>
      <div class="row"><span>Patches</span><span>$ 5</span></div>
    </div>
  </div>
</section>

</body>
</html>
```